Career Pathway Infographic - HVAC Company

We are looking for an engaging career pathway info graphic that keeps within our brand our website is www.marrowfinchheating.com

Attached you will find a rough outline along with word document of roles and responsibilities

we would like an infographic that allows employees to easily see where they are and what they need to do to reach the next level ensure use of colours, trees and logo is inkeeping with our brand

```html
<!DOCTYPE html>
<html lang="en">
<head>
<meta charset="utf-8">
<title>Career Pathway – Marrowfinch Home Services</title>
<link rel="stylesheet" href="https://fonts.googleapis.com/css2?family=Baloo+2:wght@700;800&family=Montserrat:wght@400;600;700;800&display=swap">
<style>
:root{
  --green-deep:#0b6457;
  --green:#128a78;
  --green-light:#1aa08c;
  --copper:#b8713b;
  --copper-light:#d08a4e;
  --white:#ffffff;
  --text:#e9f5f2;
}
*{margin:0;padding:0;box-sizing:border-box}
html,body{width:1200px;height:1000px;overflow:hidden}
body{background:var(--white);font-family:"Montserrat",sans-serif;color:var(--text)}
.poster{position:relative;width:1200px;height:1000px;
  background:radial-gradient(ellipse at 62% 45%,var(--green-light) 0%,var(--green) 40%,var(--green-deep) 100%);overflow:hidden}
.frame-white{position:absolute;left:12px;top:14px;right:12px;bottom:14px;border:6px solid var(--white)}
.frame-copper{position:absolute;left:28px;top:33px;right:28px;bottom:33px;border:6px solid var(--copper)}

.brand{position:absolute;left:90px;top:128px;display:flex;align-items:center;gap:14px}
.brand-mark{flex:none;width:26px;height:26px;border-radius:50%;background:var(--copper)}
.brand-name{font-family:"Montserrat",sans-serif;font-weight:800;font-size:21px;line-height:1.1;color:var(--white);width:200px}

.avatar{position:absolute;width:78px;height:126px;border-radius:38px 38px 8px 8px;
  background:linear-gradient(180deg,var(--copper-light),var(--copper))}
.arrow{position:absolute;width:40px;height:48px}
.corner{position:absolute;width:24px;height:24px;background:linear-gradient(135deg,var(--copper-light),var(--copper));
  clip-path:polygon(100% 0,100% 100%,0 100%)}
.bracket{position:absolute;width:146px;height:124px;border-top:16px solid var(--copper);border-left:17px solid var(--copper)}

.role{position:absolute}
.role-title{font-family:"Baloo 2",sans-serif;font-weight:800;font-size:23px;line-height:.95;color:var(--white)}
.role-title small{display:block;font-size:11px;line-height:1.3;margin-top:2px}
.label{font-size:7.6px;font-weight:700;letter-spacing:1.6px;color:var(--white);margin:0 0 7px}
.label.plain{letter-spacing:.2px}
.col p{font-size:7.6px;line-height:1.25;margin-bottom:9px;text-align:left;letter-spacing:.3px}
.col.wide p{letter-spacing:.7px;line-height:1.4}
.dense p{font-size:6.2px;line-height:1.42;margin:0;text-align:justify}
.dense b{font-weight:700;color:var(--white)}
.dense .gap{height:10px}

.headline{position:absolute;left:88px;top:884px;font-family:"Montserrat",sans-serif;font-weight:800;font-size:57px;letter-spacing:-1px;white-space:nowrap}
.headline .solid{color:var(--white)}
.headline .outline{color:transparent;-webkit-text-stroke:1.5px var(--white);font-weight:400}
.site{position:absolute;left:1142px;top:262px;writing-mode:vertical-rl;transform:rotate(180deg);
  font-size:11px;font-weight:600;letter-spacing:7px;color:var(--white)}
</style>
</head>
<body>
<main class="poster">
  <div class="frame-white"></div>
  <div class="frame-copper"></div>

  <header class="brand">
    <div class="brand-mark"></div>
    <div class="brand-name">Marrowfinch Home Services</div>
  </header>

  <!-- Helper -->
  <div class="avatar" style="left:110px;top:274px" role="img" aria-label="Illustrated portrait of a helper"></div>
  <svg class="arrow" style="left:228px;top:290px" viewBox="0 0 40 48"><path d="M4 0 L40 24 L18 48 L28 24 Z" fill="#fff"/><circle cx="12" cy="24" r="5" fill="#b8713b"/></svg>
  <div class="corner" style="left:251px;top:374px"></div>
  <div class="bracket" style="left:92px;top:422px"></div>
  <section class="role col" style="left:116px;top:474px;width:138px">
    <h2 class="role-title" style="margin-bottom:36px">Helper</h2>
    <h3 class="label">INTERMEDIATE SKILLS AND KNOWLEDGE</h3>
    <p>Basic understanding of HVAC and refrigeration systems.</p>
    <p>Familiarity with common hand tools and equipment used in installations.</p>
    <p>Basic safety protocols and procedures in a construction or installation setting.</p>
    <p>Ability to follow instructions and assist in basic tasks such as carrying materials, cleaning work areas, and preparing installation sites.</p>
    <h3 class="label plain">RESPONSIBILITIES</h3>
    <p>Assisting in the installation of heat pumps under supervision.</p>
    <p>Maintaining tools and equipment.</p>
    <p>Helping in loading and unloading materials and equipment.</p>
    <p>Performing cleanup tasks at the installation site.</p>
  </section>

  <!-- Junior Installer -->
  <div class="avatar" style="left:318px;top:222px" role="img" aria-label="Illustrated portrait of a junior installer"></div>
  <svg class="arrow" style="left:435px;top:222px" viewBox="0 0 40 48"><path d="M4 0 L40 24 L18 48 L28 24 Z" fill="#fff"/><circle cx="12" cy="24" r="5" fill="#b8713b"/></svg>
  <div class="corner" style="left:458px;top:322px"></div>
  <div class="bracket" style="left:300px;top:370px"></div>
  <section class="role col" style="left:326px;top:420px;width:142px">
    <h2 class="role-title" style="margin-bottom:26px">Junior<br>Installer</h2>
    <h3 class="label">INTERMEDIATE SKILLS AND KNOWLEDGE</h3>
    <p>Good knowledge of HVAC systems, especially residential heat pumps.</p>
    <p>Ability to read and interpret installation blueprints and manuals.</p>
    <p>Basic troubleshooting skills for common issues in heat pumps. Understanding of electrical systems and wiring as related to heat pump installations.</p>
    <h3 class="label plain">RESPONSIBILITIES</h3>
    <p>Assisting in more complex aspects of installation, including wiring and configuring systems.</p>
    <p>Performing basic diagnostic tests under supervision.</p>
    <p>Providing customer support and answering basic queries regarding maintenance and operation.</p>
    <p>Ensuring compliance with local building codes and regulations.</p>
    <p>Able to install basic installs by themselves.</p>
  </section>

  <!-- Lead Installer -->
  <div class="avatar" style="left:525px;top:172px" role="img" aria-label="Illustrated portrait of a lead installer"></div>
  <svg class="arrow" style="left:642px;top:170px" viewBox="0 0 40 48"><path d="M4 0 L40 24 L18 48 L28 24 Z" fill="#fff"/><circle cx="12" cy="24" r="5" fill="#b8713b"/></svg>
  <div class="corner" style="left:665px;top:270px"></div>
  <div class="bracket" style="left:507px;top:320px"></div>
  <section class="role col wide" style="left:533px;top:368px;width:145px">
    <h2 class="role-title" style="margin-bottom:26px">Lead<br>Installer</h2>
    <h3 class="label">INTERMEDIATE SKILLS AND KNOWLEDGE</h3>
    <p>Expert knowledge of heat pump systems, including installation, maintenance, and repair.</p>
    <p>Proficiency in troubleshooting complex issues and providing solutions.</p>
    <p>In-depth understanding of local building codes, regulations, and safety standards.</p>
    <p>Leadership skills to manage a team of installers.</p>
    <h3 class="label plain" style="margin-top:12px">RESPONSIBILITIES</h3>
    <p>Leading and overseeing the installation of heat pump systems.</p>
    <p>Training and mentoring junior staff and helpers.</p>
    <p>Liaising with clients, conducting site assessments, and providing recommen-dations.</p>
    <p>Ensuring the highest standards of quality and safety are met. Autonomous on managing schedule and install.</p>
  </section>

  <!-- Operations Manager -->
  <div class="avatar" style="left:728px;top:120px" role="img" aria-label="Illustrated portrait of an operations manager"></div>
  <svg class="arrow" style="left:845px;top:118px" viewBox="0 0 40 48"><path d="M4 0 L40 24 L18 48 L28 24 Z" fill="#fff"/><circle cx="12" cy="24" r="5" fill="#b8713b"/></svg>
  <div class="corner" style="left:868px;top:218px"></div>
  <div class="bracket" style="left:710px;top:268px"></div>
  <section class="role dense" style="left:736px;top:312px;width:160px">
    <h2 class="role-title" style="margin-bottom:20px">Operations<br>Manager<small>(HVAC Company)</small></h2>
    <p><b>Technical Proficiency:</b> In-depth knowledge of HVAC systems, equipment, and technologies to effectively oversee field service operations.</p>
    <p><b>Leadership:</b> Ability to lead and motivate a team of field service technicians, ensuring they deliver high-quality service to clients.</p>
    <p><b>Customer Service:</b> Strong customer-centric focus with excellent communication and interpersonal skills to handle client interactions and address concerns.</p>
    <p><b>Problem-solving:</b> Aptitude for identifying and resolving complex technical issues efficiently to minimize downtime and maximize customer satisfaction.</p>
    <p><b>Planning and Organization:</b> Skillful in planning and organizing field service schedules, ensuring timely and efficient delivery of services.</p>
    <p><b>Team Management:</b> Ability to recruit, train, and manage a team of field service technicians, fostering a positive and collaborative work environment.</p>
    <p><b>Safety Compliance:</b> Knowledge of safety regulations and protocols to ensure a safe working environment for field service technicians and compliance with industry standards.</p>
    <div class="gap"></div>
    <p><b>Oversee Field Operations:</b> Manage and coordinate field service operations to ensure timely and efficient delivery of HVAC services.</p>
    <p><b>Team Leadership:</b> Provide leadership to the field service team, including hiring, training, and performance management.</p>
    <p><b>Client Interaction:</b> Build and maintain strong client relationships, addressing their needs and ensuring a high level of customer satisfaction.</p>
    <p><b>Technical Support:</b> Provide technical support to field service technicians, troubleshooting complex issues and ensuring quality service delivery.</p>
    <p><b>Schedule Management:</b> Plan and organize field service schedules, optimizing technician routes and resource allocation.</p>
    <p><b>Quality Assurance:</b> Implement and enforce quality assurance processes to maintain high service standards and customer satisfaction.</p>
    <p><b>Safety Compliance:</b> Ensure that field service operations adhere to safety regulations and standards to create a secure work environment.</p>
    <p><b>Reporting:</b> Generate reports on field service performance, analyzing data to identify areas for improvement and implementing corrective actions.</p>
  </section>

  <!-- Field Service Manager -->
  <div class="avatar" style="left:926px;top:68px" role="img" aria-label="Illustrated portrait of a field service manager"></div>
  <div class="corner" style="left:1066px;top:166px"></div>
  <div class="bracket" style="left:909px;top:216px"></div>
  <section class="role dense" style="left:935px;top:260px;width:154px">
    <h2 class="role-title" style="margin-bottom:20px">Field Service<br>Manager<small>(HVAC Company)</small></h2>
    <p><b>Strategic Planning:</b> Ability to develop and implement strategic plans to optimize operational efficiency and meet business objectives.</p>
    <p><b>Budget Management:</b> Proficient in budgeting and financial management to ensure cost-effective operations and resource allocation.</p>
    <p><b>Process Improvement:</b> Skillful in identifying and implementing process improvements to enhance overall operational efficiency.</p>
    <p><b>Leadership and Team Management:</b> Strong leadership skills to guide and manage operational teams, fostering collaboration and a positive work culture.</p>
    <p><b>Vendor Management:</b> Experience in managing relationships with suppliers and vendors to ensure timely and cost-effective procurement of materials and services.</p>
    <p><b>Inventory Control:</b> Knowledge of inventory management practices to maintain optimal stock levels and minimize wastage.</p>
    <p><b>Regulatory Compliance:</b> Ensure compliance with industry regulations, codes, and standards related to HVAC operations.</p>
    <p><b>Communication:</b> Excellent communication skills to liaise with different departments, clients, and stakeholders to ensure smooth operations.</p>
    <div class="gap"></div>
    <p><b>Strategic Planning:</b> Develop and implement strategic plans to optimize operational processes and achieve business goals.</p>
    <p><b>Budget Oversight:</b> Manage and control operational budgets, ensuring efficient resource allocation and cost management. Identify and implement process improvements to enhance operational efficiency and reduce costs.</p>
    <p><b>Team Management:</b> Lead and manage operational teams, providing guidance and support to achieve operational excellence.</p>
    <p><b>Vendor Relations:</b> Establish and maintain strong relationships with suppliers and vendors to ensure timely and cost-effective procurement.</p>
    <p><b>Inventory Management:</b> Oversee inventory control measures to maintain optimal stock levels and minimize wastage.</p>
    <p><b>Compliance:</b> Ensure compliance with industry regulations, codes, and standards relevant to HVAC operations.</p>
    <p><b>Reporting:</b> Generate and analyze operational reports, providing insights and recommendations for continuous improvement.</p>
  </section>

  <h1 class="headline"><span class="solid">CAREER</span> <span class="outline">PATHWAY</span></h1>
  <div class="site">WWW.MARROWFINCHHEATING.COM</div>
</main>
</body>
</html>
```